Digital Book Cover

I am currently in the process of building a digital book for my web site but struggling with the front and back covers. We are an ecommerce business selling notice boards of all kind, indoor, outdoor, hospitality, staff boards, whiteboards, mobile and so on.

The company web site is orange and white. We already have a company logo which we would like included. The logo is simply the word "brightwall" in black and the work "company" in orange. When our web site was redesigned the company that designed it reversed the colours of the logo and had the word "brightwall" in black & "company" in white onto an orange banner. Either way I don't mind.

Target Market(s)

We sell to everyone online including schools colleges, universities, CWB, companies, churches, supermarkets, hotels etc. If fact everyone!

Industry/Entity Type

Digital

Requirements
Must have
• Company colours and include the company logo and strap line "A Notice Board For Every Location"
• Company details including postal address, phone, fax, email and web site.
• Finish cover to be supplied as a PDF

```html
<!DOCTYPE html>
<html lang="en">
<head>
<meta charset="utf-8">
<title>Brightwall Company – Back Cover</title>
<link rel="stylesheet" href="https://fonts.googleapis.com/css2?family=Arimo:wght@400&display=swap">
<style>
  :root {
    --orange-top: #e6a614;
    --orange-bottom: #fbb520;
    --ring-white: #ffffff;
    --ring-fill-light: #f9dca0;
    --ring-fill-warm: #f5c35a;
    --ink-dark: #231f20;
    --ink-light: #ffffff;
  }
  * { margin: 0; padding: 0; box-sizing: border-box; }
  html, body {
    width: 848px;
    height: 1200px;
    overflow: hidden;
    background: var(--orange-bottom);
  }
  .back-cover {
    position: relative;
    width: 848px;
    height: 1200px;
    overflow: hidden;
    background: linear-gradient(to bottom, var(--orange-top) 0%, var(--orange-bottom) 100%);
    font-family: "Arimo", Arial, sans-serif;
  }
  .ring-decoration {
    position: absolute;
    inset: 0;
    width: 848px;
    height: 1200px;
  }
  .company-details {
    position: absolute;
    left: 56px;
    top: 914px;
    line-height: 1;
  }
  .company-details p { white-space: nowrap; }
  .company-name   { color: var(--ink-dark);  font-size: 30px; }
  .postal-line-1  { color: var(--ink-light); font-size: 33px; margin-top: 12px; }
  .postal-line-2  { color: var(--ink-light); font-size: 22.5px; margin-top: 14px; }
  .phone-fax      { color: var(--ink-light); font-size: 19.5px; margin-top: 30px; }
  .email          { color: var(--ink-dark);  font-size: 23px; margin-top: 14px; }
  .website        { color: var(--ink-dark);  font-size: 26px; margin-top: 12px; }
</style>
</head>
<body>
  <main class="back-cover">
    <svg class="ring-decoration" viewBox="0 0 848 1200" aria-hidden="true">
      <defs>
        <linearGradient id="ringFill" x1="0" y1="0" x2="1" y2="0">
          <stop offset="0" stop-color="var(--ring-fill-light)" stop-opacity="0.85"/>
          <stop offset="1" stop-color="var(--ring-fill-warm)" stop-opacity="0.6"/>
        </linearGradient>
      </defs>
      <circle cx="1195" cy="544" r="530" fill="var(--ring-white)"/>
      <circle cx="1195" cy="544" r="425" fill="url(#ringFill)"/>
    </svg>

    <section class="company-details">
      <p class="company-name">Brightwall Company (UK) Ltd</p>
      <p class="postal-line-1">Harbour House - PO Box 4172</p>
      <p class="postal-line-2">Leamington - Warwickshire - CV31 2QX</p>
      <p class="phone-fax">Phone: 01632 960418 - Fax: 01632 960527</p>
      <p class="email">Email: sales@brightwallcompany.com</p>
      <p class="website">Web: www.brightwallcompany.com</p>
    </section>
  </main>
</body>
</html>
```